Brindlewood Business Card Design

Small Company
looking to ramp up work need business cards sick of everyone asking for a card
client base is broad.
keep it simple
Just want on the reverse of the card somewhere for me to write details for clients
appointments etc..
want to use the phrase
"Your safe, reliable and trust worthy Tradesmen"

Industry/Entity Type

Business

Contact Information for Business Card

Brindlewood Electrical Solutions Pty Ltd
Director Gregory Brindlewood
email - brindlewoodelectricalsolutions@zentromail.net
Ph - 03 95418276
Mobile - 0417592836
Domestic, Industrial, Commercial & Mining
Electrical, Solar, Communications & Fibre
REC: 41873

```html
<!DOCTYPE html>
<html lang="en">
<head>
<meta charset="utf-8">
<title>Brindlewood Electrical Solutions – Business Card</title>
<link href="https://fonts.googleapis.com/css2?family=Lato:wght@400;700;900&display=swap" rel="stylesheet">
<style>
  :root {
    --brand-blue: #3b4a9c;
    --band-blue: #34449a;
    --brand-red: #d8323c;
    --card-white: #f7f7f5;
    --backdrop: #e7e3da;
    --rule-blue: #3b4a9c;
  }
  * { box-sizing: border-box; margin: 0; padding: 0; }
  html, body {
    width: 1200px; height: 1000px; overflow: hidden;
    background: var(--backdrop);
    font-family: "Lato", Arial, sans-serif;
  }
  .stage { position: relative; width: 1200px; height: 1000px; }

  .card {
    position: absolute;
    width: 640px; height: 366px;
    background: var(--card-white);
    box-shadow: 0 2px 0 #dcdcd8, 0 4px 0 #cfcfca, 0 14px 28px rgba(0,0,0,.18);
    overflow: hidden;
  }

  /* ---------- Reverse: appointment card ---------- */
  .card--appointment { left: 70px; top: 80px; }
  .appt-title {
    position: absolute; left: 0; right: 0; top: 34px;
    text-align: center; color: var(--brand-blue);
    font-weight: 900; font-size: 26px; letter-spacing: 2px;
  }
  .appt-days {
    position: absolute; left: 60px; right: 60px; top: 84px;
    display: flex; justify-content: space-between;
    color: var(--brand-red); font-weight: 700; font-size: 17px;
  }
  .appt-date {
    position: absolute; left: 60px; top: 122px;
    color: var(--brand-blue); font-weight: 900; font-size: 20px;
    display: flex; align-items: flex-end; gap: 6px;
  }
  .appt-date .blank { display: inline-block; border-bottom: 2px solid var(--rule-blue); height: 22px; }
  .appt-date .blank--day { width: 150px; }
  .appt-date .blank--time { width: 140px; }
  .appt-for {
    position: absolute; left: 60px; right: 60px; top: 160px;
    text-align: center; color: var(--brand-red); font-size: 11px;
  }
  .appt-for-line {
    position: absolute; left: 60px; right: 60px; top: 196px;
    border-bottom: 2px solid var(--rule-blue);
  }
  .appt-notice {
    position: absolute; left: 0; right: 0; top: 206px;
    text-align: center; color: var(--brand-red); font-size: 12px; line-height: 1.25;
  }
  .appt-tagline {
    position: absolute; left: 0; right: 0; top: 250px;
    text-align: center; color: var(--brand-blue); font-weight: 700; font-size: 17px;
  }
  .wordmark {
    display: flex; align-items: center; gap: 10px;
    color: var(--brand-blue); font-weight: 700; white-space: nowrap;
  }
  .wordmark__dot { width: 14px; height: 14px; border-radius: 50%; background: var(--brand-red); flex: none; }
  .card--appointment .wordmark { position: absolute; left: 40px; top: 296px; font-size: 24px; }

  /* ---------- Front: contact card ---------- */
  .card--contact { left: 490px; top: 560px; }
  .rec-number {
    position: absolute; right: 40px; top: 24px;
    color: var(--brand-red); font-weight: 900; font-size: 19px; letter-spacing: .5px;
  }
  .card--contact .wordmark {
    position: absolute; left: 0; right: 0; top: 60px;
    justify-content: center; font-size: 32px;
  }
  .contact-tagline {
    position: absolute; left: 0; right: 0; top: 110px;
    text-align: center; color: var(--brand-blue); font-size: 14px;
  }
  .contact-name {
    position: absolute; left: 0; right: 0; top: 142px;
    text-align: center; color: var(--brand-blue); font-weight: 900; font-size: 28px;
  }
  .contact-role {
    position: absolute; left: 0; right: 0; top: 178px;
    text-align: center; color: var(--brand-red); font-weight: 900; font-size: 16px; letter-spacing: 4px;
  }
  .contact-phones {
    position: absolute; left: 70px; right: 70px; top: 210px;
    display: flex; justify-content: space-between;
    color: var(--brand-red); font-weight: 900; font-size: 17px;
  }
  .contact-email {
    position: absolute; left: 0; right: 0; top: 238px;
    text-align: center; color: var(--brand-blue); font-weight: 900; font-size: 15px;
  }
  .services-rule {
    position: absolute; left: 0; right: 0; top: 283px;
    height: 2px; background: var(--brand-red);
  }
  .services-band {
    position: absolute; left: 0; right: 0; bottom: 0; height: 76px;
    background: var(--band-blue); color: #fff;
    display: flex; align-items: center; justify-content: center;
    font-size: 14px; letter-spacing: .3px; text-align: center; line-height: 1.4;
    padding: 0 30px;
  }
</style>
</head>
<body>
<main class="stage">

  <section class="card card--appointment" aria-label="Appointment card, reverse side">
    <h2 class="appt-title">Next Appointment</h2>
    <div class="appt-days">
      <span>Sun</span><span>Mon</span><span>Tue</span><span>Wed</span><span>Thu</span><span>Fri</span><span>Sat</span>
    </div>
    <div class="appt-date">
      <span>Date :</span><span class="blank blank--day"></span>
      <span>at</span><span class="blank blank--time"></span>
      <span>pm/am</span>
    </div>
    <p class="appt-for">for</p>
    <div class="appt-for-line"></div>
    <p class="appt-notice">If unable to keep appointment kindly<br>give a 24 hour notice.</p>
    <p class="appt-tagline">"Your safe, reliable and trust worthy Tradesmen"</p>
    <div class="wordmark"><span class="wordmark__dot"></span><span>Brindlewood Electrical Solutions</span></div>
  </section>

  <section class="card card--contact" aria-label="Business card, front side">
    <p class="rec-number">REC: 41873</p>
    <div class="wordmark"><span class="wordmark__dot"></span><span>Brindlewood Electrical Solutions</span></div>
    <p class="contact-tagline">"Your safe, reliable and trust worthy Tradesmen"</p>
    <h1 class="contact-name">Gregory Brindlewood</h1>
    <p class="contact-role">Director</p>
    <div class="contact-phones">
      <span>Ph - 03 95418276</span>
      <span>Mobile - 0417592836</span>
    </div>
    <p class="contact-email">brindlewoodelectricalsolutions@zentromail.net</p>
    <div class="services-rule"></div>
    <div class="services-band">Domestic, Industrial, Commercial &amp; Mining Electrical, Solar, Communications &amp; Fibre</div>
  </section>

</main>
</body>
</html>
```